A friend who listens

find a friend who listens. place holder site:

http://afriendwholistens-example.com/

Coding

Coded - Design and coding required

Number of Pages Required

5+ page

Colors

Designer to choose colors to be used in the design.

```html
<!DOCTYPE html>
<html lang="en">
<head>
<meta charset="utf-8">
<title>A friend who listens</title>
<link href="https://fonts.googleapis.com/css2?family=Montserrat:wght@600;700&family=Open+Sans:ital,wght@0,400;0,600;1,400&display=swap" rel="stylesheet">
<style>
:root{
  --purple:#5b1a86;
  --purple-deep:#4a1270;
  --red:#c3261d;
  --orange:#e2531d;
  --ink:#111;
  --text:#333;
  --white:#fff;
  --black:#000;
}
*{margin:0;padding:0;box-sizing:border-box}
html,body{width:1200px;height:3582px;overflow:hidden;background:var(--white)}
body{position:relative;font-family:"Open Sans",sans-serif;color:var(--text)}
.abs{position:absolute}
h1,h2,h3{font-family:"Montserrat",sans-serif;color:var(--ink);font-weight:700}
.btn{position:absolute;display:flex;align-items:center;justify-content:center;border-radius:30px;font-weight:600;color:var(--white);font-size:16px;text-decoration:none}
.btn-warm{background:linear-gradient(90deg,var(--purple-deep),var(--red) 40%,var(--orange))}

/* header */
.brand{left:90px;top:10px;display:flex;align-items:center;gap:14px}
.brand-dot{width:84px;height:84px;border-radius:50%;background:var(--red)}
.brand-name{font-family:"Montserrat",sans-serif;font-weight:700;font-size:26px;line-height:1.05;color:var(--purple);width:200px}
.top-phone{right:90px;top:16px;font-size:18px;font-weight:600;color:var(--ink);display:flex;align-items:center;gap:10px}
.top-phone .num{color:var(--red);font-family:"Montserrat",sans-serif;font-size:20px}
.nav{left:406px;top:58px;width:794px;height:46px;background:var(--purple);border-radius:24px 0 0 24px;display:flex;align-items:center;padding-left:85px;gap:38px}
.nav a{color:var(--white);font-size:16px;font-weight:600;text-decoration:none}

/* hero */
.hero{left:0;top:104px;width:1200px;height:680px;background:linear-gradient(100deg,#d9d4cf,#eceae7 40%,#c9ccd1 70%,#9aa4b0)}
.hero-title{left:0;top:300px;width:1200px;text-align:center;font-size:56px;line-height:60px}
.hero-call{left:432px;top:445px;width:336px;height:52px;font-size:20px;font-weight:400;gap:10px}
.arrow{width:42px;height:42px;border-radius:50%;background:rgba(90,90,90,.75);top:358px;display:flex;align-items:center;justify-content:center}

/* feature rows */
.photo-round{border-radius:50%}
.feature-text h2{font-size:44px;line-height:52px}
.feature-text p{font-size:15.5px;line-height:29.5px;text-align:justify;margin-top:18px}

/* band */
.band{left:0;top:1437px;width:1200px;height:483px;background:linear-gradient(180deg,#6a2a8e,#a8344f 55%,#d9482a)}
.band h2{color:var(--white);font-size:46px;text-align:center;position:absolute;top:135px;width:100%}
.band p{color:var(--white);font-size:16px;line-height:30px;text-align:center;position:absolute;top:205px;left:250px;width:700px}

/* news */
.news-title{left:0;top:2575px;width:1200px;text-align:center;font-size:38px}
.card{top:2642px;width:308px;height:361px;background:var(--white);box-shadow:0 2px 8px rgba(0,0,0,.2)}
.card-img{height:245px}
.card .tag{font-style:italic;color:#666;font-size:16px;margin:16px 20px 8px}
.card h3{font-family:"Open Sans",sans-serif;font-weight:600;font-size:17.5px;line-height:27px;margin:0 20px}

/* footer */
.foot h4{font-family:"Montserrat",sans-serif;font-weight:600;color:var(--white);font-size:22px}
.foot{color:var(--white);font-size:14px;line-height:27px;top:3280px}
.foot ul{list-style:none;margin-top:16px}
.divider{top:3295px;width:1px;height:190px;background:#333}
.field{left:830px;top:3390px;width:242px;height:40px;background:var(--white);font-size:11px;color:#888;padding:12px 14px}
.send{left:1072px;top:3390px;width:42px;height:40px;background:var(--red);display:flex;align-items:center;justify-content:center}
.social{top:3461px;width:34px;height:34px;border-radius:50%}
.copy{left:0;top:3540px;width:1200px;text-align:center;color:var(--white);font-size:11px}
</style>
</head>
<body>

<!-- header -->
<div class="abs brand"><span class="brand-dot"></span><span class="brand-name">A friend who listens</span></div>
<div class="abs top-phone">Talk To Us :
  <svg width="18" height="18" viewBox="0 0 24 24"><path fill="#c3261d" d="M6.6 10.8a15 15 0 0 0 6.6 6.6l2.2-2.2c.3-.3.7-.4 1-.2 1.1.4 2.3.6 3.6.6.6 0 1 .4 1 1V20c0 .6-.4 1-1 1A17 17 0 0 1 3 4c0-.6.4-1 1-1h3.5c.6 0 1 .4 1 1 0 1.3.2 2.5.6 3.6.1.3 0 .7-.2 1z"/></svg>
  <span class="num">+1 555 010 2030</span></div>
<nav class="abs nav"><a href="#">Home</a><a href="#">About Us</a><a href="#">Talk to Us</a><a href="#">Help</a><a href="#">Support</a><a href="#">Contact Us</a>
  <svg width="16" height="16" viewBox="0 0 24 24"><circle cx="10" cy="10" r="7" fill="none" stroke="#fff" stroke-width="3"/><path d="M15 15l6 6" stroke="#fff" stroke-width="3"/></svg></nav>

<!-- hero -->
<div class="abs hero" role="img" aria-label="Photo of a counsellor listening to a woman on a sofa"></div>
<svg class="abs" style="left:0;top:600px" width="1200" height="230" viewBox="0 0 1200 230">
  <path d="M0 50 Q600 290 1200 50 L1200 230 L0 230Z" fill="#fff"/>
  <path d="M60 80 Q600 230 1140 80" fill="none" stroke="#5b1a86" stroke-width="6"/>
  <circle cx="600" cy="155" r="34" fill="#fff" stroke="#eee" stroke-width="2"/>
  <circle cx="600" cy="155" r="24" fill="#c3261d"/>
</svg>
<h1 class="abs hero-title">Stop Feeling Isolated<br>Talk to us</h1>
<a class="btn btn-warm hero-call" href="#">
  <svg width="18" height="18" viewBox="0 0 24 24"><path fill="#fff" d="M6.6 10.8a15 15 0 0 0 6.6 6.6l2.2-2.2c.3-.3.7-.4 1-.2 1.1.4 2.3.6 3.6.6.6 0 1 .4 1 1V20c0 .6-.4 1-1 1A17 17 0 0 1 3 4c0-.6.4-1 1-1h3.5c.6 0 1 .4 1 1 0 1.3.2 2.5.6 3.6.1.3 0 .7-.2 1z"/></svg>
  Call Us :&nbsp; + 1 555 010 2030</a>
<div class="abs arrow" style="left:23px"><svg width="12" height="12" viewBox="0 0 12 12"><path d="M8 1L3 6l5 5" fill="none" stroke="#fff" stroke-width="2"/></svg></div>
<div class="abs arrow" style="left:1133px"><svg width="12" height="12" viewBox="0 0 12 12"><path d="M4 1l5 5-5 5" fill="none" stroke="#fff" stroke-width="2"/></svg></div>

<!-- why people feel lonely -->
<div class="abs photo-round" style="left:250px;top:880px;width:440px;height:450px;background:radial-gradient(circle at 40% 40%,#d9b99a,#8a8a4e 60%,#5c6b36)" role="img" aria-label="Photo of an older woman resting her head in her hand, looking lonely"></div>
<div class="abs feature-text" style="left:581px;top:950px;width:434px">
  <h2>Why People Feel Lonely</h2>
  <p>Lorem ipsum dolor sit amet, consectetur adipiscing elit, sed do eiusmod tempor incididunt ut labore et dolore magna aliqua. Ut enim ad minim veniam, quis nostrud exercitation ullamco laboris nisi ut aliquip ex ea</p>
</div>
<a class="btn btn-warm" style="left:581px;top:1223px;width:157px;height:45px" href="#">Read More</a>

<!-- we provide -->
<section class="abs band" role="img" aria-label="Tinted photo of a counselling session">
  <h2>We Provide</h2>
  <p>Sed ut perspiciatis unde omnis iste natus error sit voluptatem accusantium doloremque laudantium, totam rem aperiam, eaque ipsa quae ab illo inventore veritatis</p>
  <a class="btn" style="left:432px;top:295px;width:157px;height:44px;background:var(--purple)" href="#">View Details</a>
  <a class="btn" style="left:612px;top:295px;width:157px;height:44px;border:2px solid #fff" href="#">Talk To Us</a>
</section>

<!-- trusting others -->
<div class="abs photo-round" style="left:577px;top:2020px;width:436px;height:462px;background:radial-gradient(circle at 55% 45%,#e8b07a,#b5693a 55%,#6e7a3c)" role="img" aria-label="Photo of a young woman covering her face with her hands"></div>
<div class="abs feature-text" style="left:248px;top:2100px;width:435px">
  <h2>Trusting Others</h2>
  <p>Lorem ipsum dolor sit amet, consectetur adipiscing elit, sed do eiusmod tempor incididunt ut labore et dolore magna aliqua. Ut enim ad minim veniam, quis nostrud exercitation ullamco laboris nisi ut aliquip ex ea commodo consequat. Duis aute irure dolor in reprehenderit in voluptate velit esse cillum dolore eu fugiat nulla pariatur.</p>
</div>
<a class="btn btn-warm" style="left:248px;top:2373px;width:157px;height:45px" href="#">Read More</a>

<!-- news -->
<h2 class="abs news-title">News &amp; Updates</h2>
<article class="abs card" style="left:117px"><div class="card-img" style="background:linear-gradient(135deg,#cbbfb3,#8d7f74)" role="img" aria-label="Photo of a family in a counselling session"></div><p class="tag">Lorem ipsum</p><h3>Sed ut perspiciatis unde omnis iste natus error sit</h3></article>
<article class="abs card" style="left:446px"><div class="card-img" style="background:linear-gradient(135deg,#6f6a66,#2f2d2c)" role="img" aria-label="Photo of an upset man beside a woman"></div><p class="tag">Lorem ipsum</p><h3>Sed ut perspiciatis unde omnis iste natus error sit</h3></article>
<article class="abs card" style="left:774px"><div class="card-img" style="background:linear-gradient(180deg,#b9bfc6,#5d5e60)" role="img" aria-label="Photo of a person walking alone on a beach"></div><p class="tag">Lorem ipsum</p><h3>Sed ut perspiciatis unde omnis iste natus error sit</h3></article>

<!-- footer -->
<svg class="abs" style="left:0;top:3080px" width="1200" height="502" viewBox="0 0 1200 502">
  <path d="M0 170 Q600 -20 1200 170 L1200 502 L0 502Z" fill="#000"/>
  <path d="M60 150 Q600 0 1140 150" fill="none" stroke="#5b1a86" stroke-width="6"/>
  <circle cx="600" cy="62" r="34" fill="#fff" stroke="#eee" stroke-width="2"/>
  <circle cx="600" cy="62" r="24" fill="#c3261d"/>
</svg>
<div class="abs foot" style="left:88px"><h4>Contact Us</h4>
  <p style="margin-top:16px;line-height:19px">COMPANY<br>12 Harbour Lane, Northbay 4500</p>
  <p style="margin-top:12px;line-height:19px">EMAIL ADDRESS<br>hello@afriendwholistens-example.com</p>
  <p style="margin-top:12px;line-height:19px">CALL US<br>+1 555 010 4452</p></div>
<div class="abs divider" style="left:371px"></div>
<div class="abs foot" style="left:423px"><h4>Links</h4><ul><li>Home</li><li>About Us</li><li>Talk to Us</li><li>Help</li><li>Support</li><li>Contact Us</li></ul></div>
<div class="abs divider" style="left:580px"></div>
<div class="abs foot" style="left:642px"><h4>Legal</h4><ul><li>Support</li><li>Faq</li><li>Sitemap</li><li>Contact Us</li></ul></div>
<div class="abs divider" style="left:766px"></div>
<div class="abs foot" style="left:829px;width:290px"><h4>Newsletter</h4><p style="margin-top:16px;line-height:22px">For exclusive news and updates sign up for our newsletter.</p></div>
<div class="abs field">Email Address</div>
<div class="abs send"><svg width="16" height="16" viewBox="0 0 24 24"><path d="M22 2L2 10l8 3 3 8z" fill="none" stroke="#fff" stroke-width="2"/></svg></div>
<span class="abs social" style="left:830px;background:#3b5998"></span>
<span class="abs social" style="left:877px;background:#d42020"></span>
<span class="abs social" style="left:924px;background:#dd4b39"></span>
<span class="abs social" style="left:971px;background:#1da1f2"></span>
<span class="abs social" style="left:1018px;background:#3f6db3"></span>
<p class="abs copy">© 2019 Copyrights.THE COMPANY NAME.All Rights Reserved | Privacy Policy, Terms of Service</p>

</body>
</html>
```